Harborlight Venture Studio (HVS)

Create a Flyer similar to the example or better

Target Market(s)

Management of Corporate Companies

Requirements
Must have
• follow the PDF-example
Nice to have
• compelling

```html
<!DOCTYPE html>
<html lang="en">
<head>
<meta charset="utf-8">
<title>Harborlight Venture Studio – Corporate Innovation Retreat Flyer</title>
<link href="https://fonts.googleapis.com/css2?family=Lato:wght@400;700;900&display=swap" rel="stylesheet">
<style>
:root{
  --navy:#1c1f5c;
  --gold:#c9a93f;
  --ink:#2a2a35;
  --paper:#f3f4f6;
  --mist:#dfe3e8;
  --stage:#4cb9cc;
  --sea-light:#bfe3f2;
  --sea:#2f8fa3;
  --sea-deep:#13595f;
}
*{box-sizing:border-box;margin:0;padding:0}
html,body{width:1200px;height:1200px;overflow:hidden}
body{background:var(--stage);font-family:"Lato",sans-serif;color:var(--ink);position:relative}
.sheet{position:absolute;left:222px;width:757px;height:534px;overflow:hidden;background:var(--paper)}
.sheet--outside{top:50px}
.sheet--inside{top:624px}
.sheet-art{position:absolute;inset:0;width:100%;height:100%}
.block{position:absolute}
.heading{color:var(--navy);font-weight:900;font-size:8.4px;line-height:1.25;text-transform:uppercase;letter-spacing:.1px}
.heading--center{text-align:center}
.body-text{font-size:5.5px;line-height:1.36;text-align:justify}
.body-text p{margin-bottom:4px;text-indent:4px}
.copyright{font-size:6.4px;font-weight:700;color:var(--navy);text-align:center}
.brand-mark{position:absolute;left:560px;top:96px;display:flex;align-items:center;gap:7px}
.brand-dot{width:16px;height:16px;border-radius:50%;background:var(--gold)}
.brand-name{font-weight:900;font-size:15px;color:#fff}
.footer{position:absolute;left:505px;top:468px;width:252px;color:#fff;text-align:center}
.footer-name{font-weight:900;font-size:8px}
.footer-line{font-size:5.8px;margin-top:4px;display:flex;align-items:center;justify-content:center;gap:4px}
.footer-contacts{display:flex;justify-content:center;gap:10px;margin-top:5px;font-size:5.6px;text-align:left;align-items:center}
.footer-divider{width:1px;height:16px;background:#fff}
.icon{width:8px;height:8px;flex:none}
.photo{position:absolute;width:84px;height:64px}
.day-title{color:var(--navy);font-weight:900;font-size:8px;line-height:1.25;margin-top:6px}
.day-title:first-child{margin-top:0}
.day-body{font-size:5.5px;line-height:1.36;margin-top:3px}
.day-step{font-size:5.3px;margin:3px 0 0 16px}
.side-heading{color:var(--navy);font-weight:900;font-size:8px;line-height:1.2;text-transform:uppercase;margin-top:8px}
.side-heading:first-child{margin-top:0}
.side-heading--sentence{text-transform:none}
.side-body{font-size:5.3px;line-height:1.36;margin-top:4px}
</style>
</head>
<body>

<!-- Outside spread -->
<section class="sheet sheet--outside">
  <svg class="sheet-art" viewBox="0 0 757 534" preserveAspectRatio="none">
    <defs>
      <linearGradient id="sky" x1="0" y1="0" x2="1" y2="1">
        <stop offset="0" stop-color="#d9eef8"/>
        <stop offset=".45" stop-color="#9fd0e6"/>
        <stop offset=".75" stop-color="var(--sea)"/>
        <stop offset="1" stop-color="var(--sea-deep)"/>
      </linearGradient>
      <linearGradient id="mist1" x1="0" y1="0" x2="0" y2="1">
        <stop offset="0" stop-color="var(--mist)"/>
        <stop offset="1" stop-color="#f7f8f9"/>
      </linearGradient>
    </defs>
    <rect width="757" height="534" fill="url(#mist1)"/>
    <path d="M0 150C140 200 300 222 440 196C560 170 660 140 757 136V172C670 174 590 186 520 196C400 212 240 236 0 190Z" fill="var(--gold)"/>
    <path role="img" aria-label="Photo of a surfer riding a large curling ocean wave under a clear sky" d="M0 0H757V136C660 140 560 170 440 196C300 222 140 200 0 150Z" fill="url(#sky)"/>
    <path d="M757 136C660 140 560 170 440 196C330 216 200 222 60 204C200 232 330 234 440 208C540 184 650 160 757 156Z" fill="var(--navy)"/>
    <path d="M0 496C90 498 170 508 252 526V534H0Z" fill="var(--gold)"/>
    <path d="M0 504C90 506 170 514 252 534H0Z" fill="var(--navy)"/>
    <path d="M505 478C590 452 690 450 757 462V470C690 460 590 462 505 486Z" fill="var(--gold)"/>
    <path d="M505 486C590 462 690 460 757 470V534H505Z" fill="var(--navy)"/>
  </svg>

  <div class="brand-mark">
    <span class="brand-dot"></span>
    <span class="brand-name">Tidewell-CC.com</span>
  </div>

  <h2 class="block heading heading--center" style="left:29px;top:251px;width:198px">Innovation on demand and where it originates...</h2>
  <div class="block body-text" style="left:29px;top:291px;width:198px">
    <p>The most valid and promising source of sustained innovation of your specific business will be found within your organization's collective genius and creativity. Your organization has all necessary resources for the innovation of your business at hand. The problem is: these valuable resources are either engaged in the fulfilling of your corporate traditional business requirements or they are currently struggling with the integration of an "innovative" acquisition your corporate company has to handle.</p>
    <p>How might you access and leverage the inherent genius of your organization to develop new products and services for the era of "Disruptive Innovation"? The scale of innovation your corporate business really demands will most recently not have taken place within the standard environment of the day-to-day business attitude. Innovation needs change, inspiration, and a conceptional thinking out of the box.</p>
    <p>Considering this, we have created a structured but nevertheless fully scalable and adjustable modular innovation process – innovation results based on the principals of the "Theory U" by L. M. Brandt, Design Thinking (Fieldwork Lab), Neurolinguistic Programming (NLP) and some other Agile and other SCRUM methodologies more. The complete process will be executed by the experts in your organization during (max.) 5 days, in our pre-configured agile innovation facility located and ready to use on a country estate in Italy.</p>
  </div>

  <h2 class="block heading heading--center" style="left:274px;top:251px;width:208px">Disruptive innovation and what it means for your corporate business...</h2>
  <div class="block body-text" style="left:274px;top:291px;width:208px">
    <p>As a striking example, let us briefly look at the fact and the consequence of "Disruptive Innovation" in the area of "Diabetes Care Products". Imagine – you are the owner of a production site of let's say "Diabetes Products" for which you have to implement a huge number of regulations and processes – all the while, additionally having to facilitate a remarkable value of assets, to produce products you will need for the fulfilling of your customer's needs.</p>
    <p>The corporate thinking of your organization runs on the fact of keeping your business alive, vital, and productive. You will most recently have not become aware of the fact that one huge organization, being totally out of the scope of your competitor analyses, is currently inventing a device which makes 90 percent of your products and services obsolete. And if this fact is not astonishing enough, here is one more remarkable fact: a tiny little organization and newly established business in the US, is currently developing and certifying a substituting remedy for the diabetes disease you have been creating your revenue with, over decades.</p>
    <p>And here comes the burning question to the innovation capacity of your corporate organization: how come all your experts and all your organization's expertise was not able to foresee nor to anticipate this fact of "Disruptive Innovation" of approximately 90 percent of your corporate business? How come the rights and patents are not one of your organization's assets?</p>
  </div>
  <p class="block copyright" style="left:274px;top:500px;width:208px">Copyright Tidewell Consulting &amp; Coaching LLC</p>

  <h2 class="block heading heading--center" style="left:525px;top:201px;width:212px">The current situation all "corporate businesses" are currently facing...</h2>
  <div class="block body-text" style="left:526px;top:226px;width:210px">
    <p>How your corporate business will be enabled to succeed in the era of "Disruptive Innovation"?</p>
    <p>Here is the fact: your corporate business is designed to stay in compliance with demanding regulations and it has to obey to rules of the processes. GxP, FDA and GRC and numberless additional business specific regulations and requirements are representing a framework of major influencers enabling and supporting the success of your established business and go-to-market models.</p>
    <p>We totally agree: compliance and regulations are key to operating a successful corporate business organization. However, on the other hand, there are these regulations slowing down, hindering or even disabling your capacity to innovate within the era of "Disruptive Innovation". If we talk about "Disruptive Innovation", we mean exactly that: disruption of traditional collaboration attitudes and unchanged continuation of corporate business organizations. In our era, corporate organizations of all kinds need more than just elaborating around the symptoms and trying to handle them by simple implementation attempts of new IT-infrastructures – corporate businesses need desperately a true and honest reflection upon the existing facts and in the consequence, they have to come up with valid answers to the profound challenges of the drastically changing business challenges ahead.</p>
    <p>How can you expect your corporate organization to innovate on products, processes or global synergetic collaboration, if your people and your organization are 100 percent engaged in fulfilling and ensuring the functioning of given requirements in the context of your corporate business?</p>
  </div>

  <div class="footer">
    <p class="footer-name">Tidewell™ Consulting &amp; Coaching LLC</p>
    <p class="footer-line">
      <svg class="icon" viewBox="0 0 10 10"><path d="M5 0.5A3.3 3.3 0 0 1 8.3 3.8C8.3 6.3 5 9.5 5 9.5S1.7 6.3 1.7 3.8A3.3 3.3 0 0 1 5 0.5Z" fill="var(--gold)"/><circle cx="5" cy="3.8" r="1.2" fill="var(--navy)"/></svg>
      Seeblickweg 21 CH – 6000 Uferstadt / LU
    </p>
    <div class="footer-contacts">
      <svg class="icon" style="width:12px;height:12px" viewBox="0 0 10 10"><path d="M2 1L3.6 1.2 4.2 3 3.2 3.8C3.8 5 4.9 6.1 6.1 6.7L6.9 5.7 8.8 6.3 9 8C8.5 9 7.5 9.3 6.5 8.9 4 7.8 2.1 5.9 1 3.4 0.7 2.5 1 1.5 2 1Z" fill="var(--gold)"/></svg>
      <span>+41 00 555 01 00<br>+41 00 555 01 01</span>
      <span class="footer-divider"></span>
      <span>@&nbsp; office@tidewell-cc.com<br>◎&nbsp; www.Tidewell-cc.com</span>
    </div>
  </div>
</section>

<!-- Inside spread -->
<section class="sheet sheet--inside">
  <svg class="sheet-art" viewBox="0 0 757 534" preserveAspectRatio="none">
    <defs>
      <radialGradient id="spray" cx=".5" cy=".45" r=".75">
        <stop offset="0" stop-color="#f6f7f8"/>
        <stop offset=".6" stop-color="#d7dbe0"/>
        <stop offset="1" stop-color="#b8bec6"/>
      </radialGradient>
      <linearGradient id="ocean" x1="0" y1="0" x2="1" y2="1">
        <stop offset="0" stop-color="#9ccbe0"/>
        <stop offset=".5" stop-color="var(--sea)"/>
        <stop offset="1" stop-color="var(--sea-deep)"/>
      </linearGradient>
    </defs>
    <rect role="img" aria-label="Faded photo of white wave spray behind the text" width="757" height="534" fill="url(#spray)"/>
    <path role="img" aria-label="Photo of a breaking ocean wave" d="M0 490C220 470 470 430 757 420V534H0Z" fill="url(#ocean)"/>
    <path d="M0 468C220 460 470 428 757 420V440C480 438 240 474 0 490Z" fill="var(--gold)"/>
    <path d="M330 462C500 440 640 428 757 432V444C640 440 500 452 330 470Z" fill="var(--navy)"/>
    <path d="M0 478C230 472 470 446 757 440V452C480 456 250 486 0 498Z" fill="var(--navy)"/>
  </svg>

  <div class="block" style="left:29px;top:40px;width:125px">
    <h3 class="side-heading">Our local infrastructure for this retreat (The Masseria)</h3>
    <p class="side-body">The Masseria (and Italian off-side estate) offers space for up to 10 innovators within the lovely and healthy environment of Apulia representing a totally refurbished, climatized and perfectly maintained first-class hospitality. The area also offers sufficient space for distraction and collection of thoughts, ideas and profound innovations. The intermediate HVS process steps will situationally be conducted either inside the climatized meeting rooms or on the covered country yard – or even in the form of focused off-side interventions in the open nature. The...</p>
    <h3 class="side-heading" style="margin-top:12px">How you can tailor your individual HVS process</h3>
    <p class="side-body">During the preparation of this retreat we are able to tailor the complete process to your specific needs and individualized requirements. All accommodation and dining (breakfast, lunch and dinner buffet) for the time of your innovator's stay with us is covered and ensured. Your innovators will be fully covered by a specific event-insurance.</p>
    <h3 class="side-heading" style="margin-top:12px">The investment</h3>
    <p class="side-body">As the complete process, content wise, can and will be tailored to your specific needs and expectations there is no unique price tag attached to it. Nevertheless, here is an indication of a cost tag for the HVS process (based on Theory U): € 12.000 – € 15.000 (excl. VAT) per person / 5-days. This indication has to be understood as the price including all services from the departure airport Brindisi-International and back.</p>
  </div>

  <svg class="photo" style="left:162px;top:44px" viewBox="0 0 84 64" role="img" aria-label="Photo of a bright meeting hall with tables and arched windows"><rect width="84" height="64" fill="#8f8a86"/></svg>
  <svg class="photo" style="left:162px;top:148px" viewBox="0 0 84 64" role="img" aria-label="Photo of a group of participants standing together indoors"><rect width="84" height="64" fill="#6e6a6c"/></svg>
  <svg class="photo" style="left:162px;top:254px" viewBox="0 0 84 64" role="img" aria-label="Photo of a seminar room with chairs arranged in a circle"><rect width="84" height="64" fill="#7c8486"/></svg>
  <svg class="photo" style="left:162px;top:358px" viewBox="0 0 84 64" role="img" aria-label="Photo of a dimly lit conference room with a projection screen"><rect width="84" height="64" fill="#3b4a63"/></svg>

  <div class="block" style="left:258px;top:42px;width:226px">
    <h3 class="day-title">Day 1: Downloading pattern from the past (9 hours)</h3>
    <p class="day-body">The focus of our work today, is your current situation in the context, which we defined for this particular 5 day HVS process.</p>
    <p class="day-step">Suspending</p>
    <p class="day-body">Finding and applying options and opportunities to overcome your company's traditional thinking and collaboration attitude.</p>
    <p class="day-step">Re-Directing</p>
    <p class="day-step">Letting Go</p>
    <h3 class="day-title">Day 2: Presencing and identification of the organization's blind spots (12 hours)</h3>
    <p class="day-body">The focus of our work today are questions and tasks around the purpose and sense of your current processes, attitudes and the organization's contributors. Identifying the blind spots by answering questions such as "Who is myself in the process?" and "What is my work and responsibility – on the whole".</p>
    <h3 class="day-title">Day 3: Letting the options come and crystallization of valuable solutions (12 hours)</h3>
    <p class="day-body">Text to follow</p>
    <h3 class="day-title">Day 4: Crystallization, concretization &amp; prototyping – How might we.. (12 hours)</h3>
    <p class="day-body">Text to follow</p>
    <h3 class="day-title">Day 5: Developing prototypes for processes and innovations &amp; Initiation of performing (How to get the job done...) (8 hours)</h3>
    <p class="day-body">Text to follow</p>
    <p class="day-body" style="margin-top:10px;text-align:justify">Around 16:30 the shuttle service will be waiting to transport the innovators back to Brindisi-International-Airport. Our staff will guide your innovators back to the airport the journey stared. From here your organization will have the chance and challenge to reflect, to adopt and to implement the working results of your innovators.</p>
    <p class="day-body" style="margin-top:6px;text-align:justify">The HVS process conducted during this retreat covers in total more than 50 hours of intense refection, extraction and intervention time – so the results will be profound and, once implemented, your business will be enabled toward the next level of efficiency and performance.</p>
  </div>

  <svg class="photo" style="left:488px;top:44px" viewBox="0 0 84 64" role="img" aria-label="Photo of a stone wall gate under olive trees"><rect width="84" height="64" fill="#c8c3b4"/></svg>
  <svg class="photo" style="left:488px;top:148px" viewBox="0 0 84 64" role="img" aria-label="Photo of a restored stone farmhouse with a lawn"><rect width="84" height="64" fill="#b9a78a"/></svg>
  <svg class="photo" style="left:488px;top:254px" viewBox="0 0 84 64" role="img" aria-label="Photo of a swimming pool beside a whitewashed stone hut"><rect width="84" height="64" fill="#7fa7a8"/></svg>
  <svg class="photo" style="left:488px;top:358px" viewBox="0 0 84 64" role="img" aria-label="Photo of a pool terrace with a white pavilion"><rect width="84" height="64" fill="#6fa2b4"/></svg>

  <div class="block" style="left:580px;top:44px;width:152px">
    <h3 class="side-heading side-heading--sentence">Set-up, preparation and execution...</h3>
    <p class="side-body">Our Harborlight Venture Studio (HVS) process follows the principals of the Theory U (C) approach and is based on application of Agile principals and methodologies of Design Thinking and SCRUM. The aim of the HVS process is to enable your corporate organization to anticipate the requirements of the era of "Disruptive Innovation". (1.) Our joint journey starts with the assessment of your organization's best brains – jointly we prepare your specific content and process targets – and we will integrate them into our given structure. (2.) We enable your eligible contributors with tools and methodologies – to succeed successfully with the process. (3.) During the process with facilitation at our estate in Italy, your organization's contributors will apply their technical and business competence in accordance with the principals of the HVS process. (4.) In teams, (amount to be defined) your organization's contributors are guided through the Theory "U" process – and the innovation and creation of innovative and feasible business concepts are almost guaranteed. (5.) After the completion of the HVS process, your facilitators (if you wish), with Tidewell Consulting &amp; Coaching LLC support, will ensure the implementation of the elaborated innovation in the context of your corporate organization. Important: our aim is to enable your organization to innovate on demand – we support you in the execution and the preparation of related steps on demand – and at your request.</p>
    <h3 class="side-heading side-heading--sentence" style="margin-top:10px">How the HVS process will be conducted...</h3>
    <p class="side-body">Together with your chosen management staff (your innovators) you will retreat to our pre-configured facility in Italy. We shall pick up the innovators at the import of your choice and fly with them to the international airport of Brindisi (I). From Brindisi-Airport we will guide and accompany the innovators via our shuttle service to our first-class maintained Masseria (the retreat). We will arrive there at around 10.00 a.m. After a brief welcome our process will start at around 11.00 a.m. with the first step of the U-Process:</p>
  </div>
</section>

</body>
</html>
```